Upscale business cards needed for family business

We need professional business cards created for several family members. We are a family business holding company. We would like these relatively simple and straightforward, but also with a unique element to set them apart. Probably stick with neutral and simple colors - white, grey etc. We need space for the traditional elements, including name, title, address, email/phone number. And we will be creating several from this template so it needs to be template that is easy to switch information in and out of.

Industry/Entity Type

Business

Contact Information for Business Card

Please include the attached Dunmore Ventures logo.

Requirements
Must have
• The attached Dunmore Ventures logo.

```html
<!DOCTYPE html>
<html lang="en">
<head>
<meta charset="utf-8">
<title>Dunmore Ventures Business Cards</title>
<link href="https://fonts.googleapis.com/css2?family=Source+Sans+3:wght@400;600;700&display=swap" rel="stylesheet">
<style>
  :root {
    --backdrop: #e4e4e4;
    --card: #252525;
    --gold: #e2a92b;
    --white: #f4f4f4;
  }
  * { margin: 0; padding: 0; box-sizing: border-box; }
  html, body {
    width: 1200px;
    height: 900px;
    overflow: hidden;
    background: var(--backdrop);
    font-family: "Source Sans 3", "Myriad Pro", sans-serif;
  }
  .card {
    position: absolute;
    top: 306px;
    width: 439px;
    height: 270px;
    background: var(--card);
    border-radius: 10px;
    color: var(--white);
  }
  .card--front { left: 149px; }
  .card--back { left: 608px; }

  .brand-name {
    position: absolute;
    color: var(--gold);
    font-weight: 600;
    text-align: center;
    white-space: nowrap;
    letter-spacing: 0.04em;
    transform: translate(-50%, -50%);
  }
  .card--front .brand-name {
    left: 108px;
    top: 138px;
    font-size: 17px;
  }
  .card--back .brand-name {
    left: 220px;
    top: 145px;
    font-size: 34px;
  }

  .holder {
    position: absolute;
    left: 234px;
    top: 56px;
  }
  .holder__name {
    color: var(--gold);
    font-size: 18px;
    font-weight: 700;
    line-height: 22px;
  }
  .holder__title {
    font-size: 12.5px;
    line-height: 14px;
    padding-left: 3px;
  }
  .contact-list {
    list-style: none;
    margin-top: 18px;
    font-size: 12.5px;
    line-height: 16px;
  }
  .contact-list li {
    display: flex;
    align-items: center;
    gap: 4px;
  }
  .contact-list svg {
    width: 9px;
    height: 9px;
    fill: var(--gold);
    stroke: var(--gold);
  }
  .address {
    margin-top: 13px;
    font-size: 12.5px;
    line-height: 15.5px;
  }
</style>
</head>
<body>
  <section class="card card--front" aria-label="Business card front">
    <div class="brand-name">DUNMORE VENTURES INC</div>
    <div class="holder">
      <div class="holder__name">Daniel Hargrove</div>
      <div class="holder__title">Managing Director</div>
      <ul class="contact-list">
        <li>
          <svg viewBox="0 0 10 10" aria-hidden="true"><path stroke="none" d="M1 3.5 Q5 0.5 9 3.5 L8 5 L6.5 4 L6.5 3.2 Q5 2.7 3.5 3.2 L3.5 4 L2 5 Z M2.5 5.5 L7.5 5.5 L8.5 9 L1.5 9 Z"/></svg>
          123-456-7890
        </li>
        <li>
          <svg viewBox="0 0 10 10" aria-hidden="true"><rect x="1" y="2" width="8" height="6" stroke="none"/><path d="M1 2.3 L5 5.5 L9 2.3" fill="none" stroke="#252525" stroke-width="1"/></svg>
          info@youremail.com
        </li>
        <li>
          <svg viewBox="0 0 10 10" aria-hidden="true"><path d="M4.5 3 L6 1.5 Q7 0.8 8 1.8 Q9 2.8 8.2 3.8 L6.5 5.5 M5.5 7 L4 8.5 Q3 9.2 2 8.2 Q1 7.2 1.8 6.2 L3.5 4.5 M3.5 6.5 L6.5 3.5" fill="none" stroke-width="1.1"/></svg>
          www.yourweb.com
        </li>
      </ul>
      <p class="address">1234, Address Goes Here<br>Country Name, 123456</p>
    </div>
  </section>

  <section class="card card--back" aria-label="Business card back">
    <div class="brand-name">DUNMORE VENTURES INC</div>
  </section>
</body>
</html>
```